We Brookmeade Grace Fellowship Church Need a Post card that will be an invite for just one Sunday...which is THE LAST SUNDAY of the year. We are a small church but we are pushing to have 150 the last Sunday of 2014 which is December 28th 2014...Our service will begin at 10 a.m. We will have a meal to follow service. I would like for you to help me with a nice back ground that will grab peoples attention.. and also I like to keep the same theme and make some folding Business cards to send people thank you for visiting. and also a regular size business card to slip inside that and to hand out on a daily basis... Our Web site is www.Brookmeade1stFellowship.example all our info is on there and you can kind of see our theme we are going with. and also I was wondering is it possible to push the post Cards THE LAST SUNDAY CARD so we can start handing them out... we like to have 500 of those and say 1000 Folding business cards and 1000 regular Busyness cards..

Nmae . Pastor Dale Orwin, # 555-274-8106

```html
<!DOCTYPE html>
<html lang="en">
<head>
<meta charset="utf-8">
<title>Brookmeade Grace Fellowship Church – The Last Sunday Postcard</title>
<link rel="stylesheet" href="https://fonts.googleapis.com/css2?family=Montserrat:wght@400;500;600;700&family=Marcellus&display=swap">
<style>
  :root {
    --backdrop: #a5a7aa;
    --card-white: #f7f8f9;
    --band-blue: #2c8bb8;
    --band-blue-deep: #1f76a6;
    --band-blue-light: #5aa9cf;
    --navy: #14324a;
    --ink-gray: #4a4d52;
    --logo-gray: #5b5e63;
    --accent-teal: #2a86b6;
    --frost-light: #eef1f4;
    --frost-mid: #c9ced4;
    --frost-dark: #8e949b;
    --rule-gray: #b9bcc0;
  }
  * { box-sizing: border-box; margin: 0; padding: 0; }
  html, body {
    width: 1200px; height: 687px; overflow: hidden;
    background: var(--backdrop);
    font-family: "Montserrat", Arial, sans-serif;
  }
  .canvas { position: relative; width: 1200px; height: 687px; }

  .postcard {
    position: absolute; overflow: hidden;
    background: var(--card-white);
    box-shadow: 4px 6px 8px rgba(0,0,0,.28);
  }

  /* ---------- Front ---------- */
  .postcard--front { left: 44px; top: 40px; width: 464px; height: 598px; }
  .front-photo {
    position: absolute; left: 0; top: 0; width: 464px; height: 334px;
    background:
      radial-gradient(ellipse at 55% 35%, rgba(255,255,255,.85), rgba(255,255,255,0) 60%),
      linear-gradient(180deg, var(--frost-mid) 0%, var(--frost-light) 45%, var(--frost-mid) 80%, var(--frost-dark) 100%);
  }
  .brand {
    position: absolute; display: flex; align-items: center; gap: 10px;
    color: var(--logo-gray); font-weight: 500; line-height: 1.1;
  }
  .brand__dot { flex: none; border-radius: 50%; background: var(--accent-teal); }
  .brand--front { left: 80px; top: 88px; width: 330px; font-size: 27px; }
  .brand--front .brand__dot { width: 26px; height: 26px; }

  .front-band {
    position: absolute; left: 0; top: 334px; width: 464px; height: 220px;
    background: linear-gradient(180deg, var(--band-blue-light) 0%, var(--band-blue) 40%, var(--band-blue-deep) 100%);
    color: #fff;
  }
  .front-band p, .front-band h1 { position: absolute; line-height: 1; white-space: nowrap; }
  .front-band__church {
    top: 13px; width: 100%; text-align: center;
    font-size: 15px; font-weight: 600;
  }
  .front-band__headline {
    top: 33px; width: 100%; text-align: center;
    font-family: "Marcellus", Georgia, serif; font-size: 42px; font-weight: 400; letter-spacing: 1px;
  }
  .front-band__lead {
    left: 70px; top: 87px;
    font-size: 15px; color: var(--navy);
  }
  .front-band__feature {
    left: 70px; top: 103px;
    font-family: "Marcellus", Georgia, serif; font-size: 36px; color: var(--navy);
  }
  .front-band__tail {
    right: 89px; top: 134px;
    font-size: 12px; color: var(--navy);
  }
  .front-band__date {
    left: 100px; top: 151px;
    font-size: 19px; font-weight: 500;
  }
  .front-band__date small { font-size: 13px; }
  .front-waves { position: absolute; left: 0; top: 514px; width: 464px; height: 42px; }
  .front-footer {
    position: absolute; left: 0; top: 554px; width: 464px; height: 44px;
    display: flex; align-items: center; justify-content: center;
    background: var(--frost-light);
    font-size: 13px; font-weight: 500; color: var(--navy);
  }

  /* ---------- Back ---------- */
  .postcard--back { left: 548px; top: 167px; width: 605px; height: 466px; }
  .back-photo {
    position: absolute; inset: 0;
    background:
      radial-gradient(ellipse at 30% 30%, rgba(255,255,255,.95), rgba(255,255,255,0) 55%),
      linear-gradient(180deg, #f4f5f7 0%, #e6e9ec 55%, #d3d7dc 100%);
  }
  .brand--back { left: 38px; top: 48px; width: 300px; font-size: 19px; }
  .brand--back .brand__dot { width: 20px; height: 20px; }
  .stamp-box {
    position: absolute; left: 332px; top: 45px; width: 104px; height: 88px;
    border: 2px solid var(--rule-gray);
  }
  .contact { position: absolute; left: 38px; top: 120px; color: var(--ink-gray); }
  .contact__label { font-size: 10px; font-weight: 600; margin-bottom: 10px; }
  .contact__line { font-size: 10px; font-weight: 600; line-height: 1.4; }
  .contact__pastor { font-size: 13px; font-weight: 600; margin-top: 10px; color: #2e3135; }
  .contact__web {
    position: absolute; left: 38px; top: 236px;
    font-size: 11px; font-weight: 600; color: var(--accent-teal);
  }
  .address-lines { position: absolute; left: 355px; top: 234px; width: 240px; }
  .address-lines span { display: block; height: 1px; background: var(--rule-gray); margin-bottom: 41px; }
  .back-strip {
    position: absolute; left: 0; bottom: 0; width: 100%; height: 31px;
    background: var(--band-blue);
  }
</style>
</head>
<body>
<main class="canvas">

  <section class="postcard postcard--front">
    <div class="front-photo" role="img" aria-label="Photograph of two people holding hands in a frosty winter meadow"></div>
    <div class="brand brand--front">
      <span class="brand__dot"></span>
      <span class="brand__name">Brookmeade Grace Fellowship Church</span>
    </div>

    <div class="front-band">
      <p class="front-band__church">Brookmeade Grace Fellowship Church</p>
      <h1 class="front-band__headline">INVITE YOU</h1>
      <p class="front-band__lead">for just one Sunday...which is</p>
      <p class="front-band__feature">THE LAST SUNDAY</p>
      <p class="front-band__tail">of the year.</p>
      <p class="front-band__date">December 28th 2014 <small>at 10 a.m</small></p>
    </div>

    <svg class="front-waves" viewBox="0 0 464 42" aria-hidden="true">
      <path d="M0 34 C120 14 260 12 464 26 L464 42 L0 42 Z" fill="#eef1f4"/>
      <path d="M0 26 C130 8 290 6 464 18" fill="none" stroke="#ffffff" stroke-width="2" opacity=".85"/>
      <path d="M0 31 C140 13 300 11 464 23" fill="none" stroke="#ffffff" stroke-width="1.2" opacity=".6"/>
    </svg>

    <footer class="front-footer">www.Brookmeade1stFellowship.example</footer>
  </section>

  <section class="postcard postcard--back">
    <div class="back-photo" role="img" aria-label="Faded photograph of frosted grasses in a winter field"></div>

    <div class="brand brand--back">
      <span class="brand__dot"></span>
      <span class="brand__name">Brookmeade Grace Fellowship Church</span>
    </div>

    <div class="stamp-box"></div>

    <div class="contact">
      <p class="contact__label">call or visit us at:</p>
      <p class="contact__line">(555) 318-6042</p>
      <p class="contact__line">pastororwinbgfc@example.com</p>
      <p class="contact__line">2280 Brookmeade Rd. Brookmeade Tn. 38999</p>
      <p class="contact__pastor">Pastor Dale Orwin</p>
    </div>
    <p class="contact__web">www.Brookmeade1stFellowship.example</p>

    <div class="address-lines"><span></span><span></span><span></span><span></span></div>

    <div class="back-strip"></div>
  </section>

</main>
</body>
</html>
```